Software company WebSite Design (enterprise level SW, Mobile apps, HW prototypes)

We need design for our new webpages. We got new logo and new business cards and we need webdesign which will be match with those two.
We are dealing with corporate level software development - enterprise level portals, development of optimalization SW, route planning optimalizations. For a few months we are developing mobile applications for companies.
IMPORTANT is to express the cutting edge technological company.

Target Market(s)

IT company customers

Industry/Entity Type

Business

Number of Pages Required

2 page

Requirements
Must have
• Project needs to have landing page and product detail page. Design needs to be created including full font and example images as there would be a real webpage. Design should be clean, modern and expressing hi-tech level of the company.
• Example of well designer web pages - www.quorvelt.com, www.brandissa.com - We like the font formatting and font designs (colors, placing, etc - its professional).
• Attached image contains screenshot from old web landing page. It contains basic sections of our business (Simulation Tools, Enterprise Intranet Systems, Hi-tech web presentations, Supporting Enterprise services - Optimalization and logistics monitoring)

```html
<!DOCTYPE html>
<html lang="en">
<head>
<meta charset="utf-8">
<title>KVORA — Software Development</title>
<link rel="stylesheet" href="https://fonts.googleapis.com/css2?family=Lato:wght@300;400;700&display=swap">
<style>
  :root {
    --black: #0b0b0b;
    --white: #ffffff;
    --blue: #3db3f0;
    --blue-title: #1f6fc0;
    --orange: #f26a21;
    --red-deep: #b3000d;
    --red-hot: #f0400f;
    --navy: #0a2f9e;
    --sky: #2f8fe3;
    --grey-btn: #a8a8a8;
    --text: #3b3b3b;
    --muted: #8a8a8a;
  }
  * { margin: 0; padding: 0; box-sizing: border-box; }
  html, body { width: 1200px; height: 3822px; overflow: hidden; }
  body { position: relative; background: var(--white); font-family: "Lato", sans-serif; color: var(--text); }

  .site-header { position: absolute; top: 0; left: 0; width: 1200px; height: 64px; background: var(--black); }
  .brand { position: absolute; display: flex; align-items: center; gap: 8px; color: var(--white); font-weight: 700; letter-spacing: 1px; }
  .brand-dot { width: 18px; height: 18px; background: var(--orange); }
  .site-header .brand { left: 172px; top: 18px; font-size: 26px; }
  .main-nav { position: absolute; left: 340px; top: 0; height: 64px; display: flex; align-items: center; gap: 13px; }
  .main-nav a { color: var(--white); text-decoration: none; font-size: 9.5px; font-weight: 700; letter-spacing: .3px; position: relative; }
  .main-nav a.active { color: var(--orange); }
  .main-nav a.active::after { content: ""; position: absolute; left: 0; right: 0; bottom: -8px; height: 2px; background: var(--orange); }
  .search-icon { width: 12px; height: 12px; }

  .hero { position: absolute; top: 64px; left: 0; width: 1200px; height: 550px;
    background: linear-gradient(110deg, #3a3430 0%, #6d6660 35%, #a8a39d 60%, #d9d6d2 80%, #8c8782 100%); }
  .hero-title { position: absolute; top: 270px; width: 100%; text-align: center; color: var(--white); font-size: 32px; font-weight: 400; }
  .hero-arrow { position: absolute; top: 258px; width: 30px; height: 50px; }
  .hero-arrow.prev { left: 102px; }
  .hero-arrow.next { right: 102px; }

  .section-title { position: absolute; width: 100%; text-align: center; font-size: 44px; font-weight: 300; color: #333; }

  .service { position: absolute; width: 260px; text-align: center; }
  .service-icon { width: 127px; height: 127px; margin: 0 auto; display: flex; align-items: center; justify-content: center;
    clip-path: polygon(30% 0, 70% 0, 100% 30%, 100% 70%, 70% 100%, 30% 100%, 0 70%, 0 30%); }
  .service-icon.blue { background: var(--blue); }
  .service-icon.orange { background: var(--orange); }
  .service-name { margin-top: 23px; font-size: 21px; line-height: 27px; color: #333; }
  .service-rule { width: 115px; height: 3px; margin: 27px auto 0; }
  .service-rule.blue { background: var(--blue); }
  .service-rule.orange { background: var(--orange); }
  .service-text { margin-top: 28px; font-size: 12.5px; line-height: 20px; color: var(--muted); }

  .band { position: absolute; left: 0; width: 1200px; }
  .band.red { top: 1376px; height: 637px;
    clip-path: polygon(0 0, 100% 191px, 100% 100%, 0 497px);
    background: radial-gradient(ellipse at 55% 50%, var(--red-hot) 0%, #d81a0c 35%, var(--red-deep) 75%); }
  .band.blue { top: 2489px; height: 632px;
    clip-path: polygon(0 136px, 100% 0, 100% 505px, 0 100%);
    background: linear-gradient(100deg, var(--navy) 0%, #1553c4 45%, var(--sky) 75%, #1b5fcf 100%); }

  .photo-octagon { position: absolute; width: 433px; height: 433px;
    clip-path: polygon(30% 0, 70% 0, 100% 30%, 100% 70%, 70% 100%, 30% 100%, 0 70%, 0 30%); }
  .photo-octagon.light { background: linear-gradient(135deg, #f2f2f2 0%, #bdbdbd 55%, #6f6f6f 100%); }
  .photo-octagon.warm { background: linear-gradient(135deg, #e6e6e6 0%, #9a9a9a 50%, #4a4a4a 100%); }

  .feature { position: absolute; width: 440px; }
  .feature-title { font-size: 33px; font-weight: 400; line-height: 36px; }
  .feature.on-dark .feature-title { color: var(--white); }
  .feature.on-light .feature-title { color: var(--blue-title); }
  .feature-text { margin-top: 20px; font-size: 12.5px; line-height: 21px; }
  .feature.on-dark .feature-text { color: rgba(255,255,255,.85); }
  .feature.on-light .feature-text { color: var(--muted); }
  .btn { display: inline-block; margin-top: 26px; width: 132px; height: 36px; line-height: 36px; text-align: center;
    font-size: 10px; font-weight: 700; color: var(--white); letter-spacing: .5px; }
  .btn.blue { background: var(--blue); }
  .btn.orange { background: var(--orange); }
  .btn.grey { background: var(--grey-btn); }

  .site-footer { position: absolute; top: 3644px; left: 0; width: 1200px; height: 178px; background: var(--black); text-align: center; }
  .site-footer .brand { left: 50%; transform: translateX(-50%); top: 34px; font-size: 28px; }
  .footer-nav { position: absolute; top: 104px; width: 100%; display: flex; justify-content: center; gap: 0; }
  .footer-nav a { color: var(--white); text-decoration: none; font-size: 9px; font-weight: 700; padding: 0 12px; border-left: 1px solid #666; }
  .footer-nav a:first-child { border-left: 0; }
  .copyright { position: absolute; top: 136px; width: 100%; font-size: 8px; color: #bbb; letter-spacing: .5px; }
  .to-top { position: absolute; right: 30px; top: 132px; color: #bbb; font-size: 10px; }
</style>
</head>
<body>

<header class="site-header">
  <div class="brand"><span class="brand-dot"></span>KVORA</div>
  <nav class="main-nav">
    <a class="active" href="#">O FIRME</a>
    <a href="#">SIMULACNI NASTROJE</a>
    <a href="#">INFORMACNI SYSTEMY</a>
    <a href="#">WEBOVE PREZENTACE</a>
    <a href="#">PODPURNE FIREMNI SYSTEMY</a>
    <a href="#">GRAFICKE FOTOGRAFICKE PRACE</a>
    <a href="#">CONTACT</a>
    <svg class="search-icon" viewBox="0 0 12 12"><circle cx="5" cy="5" r="3.6" fill="none" stroke="#f26a21" stroke-width="1.6"/><line x1="7.7" y1="7.7" x2="11" y2="11" stroke="#f26a21" stroke-width="1.6"/></svg>
  </nav>
</header>

<section class="hero" role="img" aria-label="Photo of business people meeting in a bright office">
  <svg class="hero-arrow prev" viewBox="0 0 30 50"><polyline points="24,6 6,25 24,44" fill="none" stroke="#fff" stroke-width="5"/></svg>
  <h1 class="hero-title">We are a software development company</h1>
  <svg class="hero-arrow next" viewBox="0 0 30 50"><polyline points="6,6 24,25 6,44" fill="none" stroke="#fff" stroke-width="5"/></svg>
</section>

<h2 class="section-title" style="top:688px">What We Provide ?</h2>

<div class="service" style="left:176px;top:798px">
  <div class="service-icon blue"><svg width="46" height="38" viewBox="0 0 46 38"><rect x="15" y="2" width="16" height="8" fill="none" stroke="#fff" stroke-width="3"/><rect x="2" y="9" width="42" height="27" rx="2" fill="#fff"/><rect x="2" y="19" width="42" height="2" fill="#3db3f0"/><rect x="20" y="16" width="6" height="8" fill="#3db3f0"/></svg></div>
  <h3 class="service-name">Enterprise<br>Level Portals</h3>
  <div class="service-rule blue"></div>
  <p class="service-text">Sed ut perspiciatis unde omnis iste natus error sit voluptatem accusantium doloremque laudantium, totam rem aperiam, eaque ipsa quae ab illo inventore veritatis et quasi architecto beatae vitae dicta sunt explicabo. Nemo enim ipsam voluptatem quia</p>
</div>
<div class="service" style="left:469px;top:798px">
  <div class="service-icon orange"><svg width="46" height="38" viewBox="0 0 46 38"><rect x="15" y="2" width="16" height="8" fill="none" stroke="#fff" stroke-width="3"/><rect x="2" y="9" width="42" height="27" rx="2" fill="#fff"/><rect x="2" y="19" width="42" height="2" fill="#f26a21"/><rect x="20" y="16" width="6" height="8" fill="#f26a21"/></svg></div>
  <h3 class="service-name">Development Of<br>Optimalization SW</h3>
  <div class="service-rule orange"></div>
  <p class="service-text">Sed ut perspiciatis unde omnis iste natus error sit voluptatem accusantium doloremque laudantium, totam rem aperiam, eaque ipsa quae ab illo inventore veritatis et quasi architecto beatae vitae dicta sunt explicabo. Nemo enim ipsam voluptatem quia</p>
</div>
<div class="service" style="left:762px;top:798px">
  <div class="service-icon orange"><svg width="46" height="38" viewBox="0 0 46 38"><rect x="15" y="2" width="16" height="8" fill="none" stroke="#fff" stroke-width="3"/><rect x="2" y="9" width="42" height="27" rx="2" fill="#fff"/><rect x="2" y="19" width="42" height="2" fill="#f26a21"/><rect x="20" y="16" width="6" height="8" fill="#f26a21"/></svg></div>
  <h3 class="service-name">Route Planning<br>Optimalizations</h3>
  <div class="service-rule orange"></div>
  <p class="service-text">Sed ut perspiciatis unde omnis iste natus error sit voluptatem accusantium doloremque laudantium, totam rem aperiam, eaque ipsa quae ab illo inventore veritatis et quasi architecto beatae vitae dicta sunt explicabo. Nemo enim ipsam voluptatem quia</p>
</div>

<h2 class="section-title" style="top:1334px">Our Business</h2>

<div class="band red"></div>
<div class="photo-octagon light" style="left:161px;top:1452px" role="img" aria-label="Photo of hands reviewing printed charts and graphs"></div>
<div class="feature on-dark" style="left:612px;top:1594px">
  <h3 class="feature-title">Simulation Tools</h3>
  <p class="feature-text">Sed ut perspiciatis unde omnis iste natus error sit voluptatem accusantium doloremque laudantium, totam rem aperiam, eaque ipsa quae ab illo inventore veritatis et quasi architecto beatae vitae dicta sunt explicabo.</p>
  <span class="btn blue">LEARN MORE</span>
</div>

<div class="feature on-light" style="left:171px;top:2132px">
  <h3 class="feature-title">Enterprise Intranet<br>Systemst</h3>
  <p class="feature-text">Sed ut perspiciatis unde omnis iste natus error sit voluptatem accusantium doloremque laudantium, totam rem aperiam, eaque ipsa quae ab illo inventore veritatis et quasi architecto beatae vitae dicta sunt explicabo.</p>
  <span class="btn grey">LEARN MORE</span>
</div>
<div class="photo-octagon light" style="left:599px;top:2034px" role="img" aria-label="Photo of a person working on a laptop"></div>

<div class="band blue"></div>
<div class="photo-octagon warm" style="left:161px;top:2612px" role="img" aria-label="Photo of a smiling man in an office"></div>
<div class="feature on-dark" style="left:609px;top:2718px">
  <h3 class="feature-title">Hi-tech Web<br>Presentations</h3>
  <p class="feature-text">Sed ut perspiciatis unde omnis iste natus error sit voluptatem accusantium doloremque laudantium, totam rem aperiam, eaque ipsa quae ab illo inventore veritatis et quasi architecto beatae vitae dicta sunt explicabo.</p>
  <span class="btn orange">LEARN MORE</span>
</div>

<div class="feature on-light" style="left:171px;top:3222px">
  <h3 class="feature-title">Supporting Enterprise<br>services Optimalization<br>and logistics monitoring</h3>
  <p class="feature-text">Sed ut perspiciatis unde omnis iste natus error sit voluptatem accusantium doloremque laudantium, totam rem aperiam, eaque ipsa quae ab illo inventore veritatis et quasi architecto beatae vitae dicta sunt explicabo.</p>
  <span class="btn grey">LEARN MORE</span>
</div>
<div class="photo-octagon warm" style="left:599px;top:3109px" role="img" aria-label="Photo of a smartphone and laptop on a desk"></div>

<footer class="site-footer">
  <div class="brand"><span class="brand-dot"></span>KVORA</div>
  <nav class="footer-nav">
    <a href="#">O FIRME</a>
    <a href="#">SIMULACNI NASTROJE</a>
    <a href="#">INFORMACNI SYSTEMY</a>
    <a href="#">WEBOVE PREZENTACE</a>
    <a href="#">PODPURNE FIREMNI SYSTEMY</a>
    <a href="#">GRAFICKE FOTOGRAFICKE PRACE</a>
    <a href="#">CONTACT</a>
  </nav>
  <p class="copyright">© 2016 COMPANY NAME | ALL RIGHTS RESERVED</p>
  <span class="to-top">▲</span>
</footer>

</body>
</html>
```